Ward Compass Business Card Design*

We need a business card design for our company Ward Compass. Our company is specialized in providing online consulting services regarding medical institutions, hospitals and doctors. We work with patients worldwide looking to choose between healthcare providers. We have a website you may use as a reference, where we list doctors and clinics worldwide. So we target Medical providers as well as patients worldwide.
Target Market(s)
Medical Providers and patients around the world
Industry/Entity Type
Medical
Contact Information for Business Card
Salma Derkaoui
CEO
+90 612 348 2071
info@wardcompass-example.com
www.wardcompass-example.com
14 Annakhil 3 H.R.B. Rabat, Morocco
Requirements
Must have
- Company logo/name on one full side, personal info and smaller logo and company name on the other side.
Nice to have
- Smart and elegant design

```html
<!DOCTYPE html>
<html lang="en">
<head>
<meta charset="utf-8">
<title>Ward Compass – Business Card</title>
<link href="https://fonts.googleapis.com/css2?family=Poppins:wght@400;500&display=swap" rel="stylesheet">
<style>
  :root {
    --bg: #e4e4e4;
    --paper: #ffffff;
    --navy: #0c3660;
    --navy-light: #1f4f80;
    --navy-deep: #123f73;
    --swoosh: #8a898b;
    --ink-light: #ffffff;
  }
  * { margin: 0; padding: 0; box-sizing: border-box; }
  html, body {
    width: 1200px; height: 1200px; overflow: hidden;
    background: var(--bg);
    font-family: "Poppins", sans-serif;
  }
  .stage {
    width: 1200px; height: 1200px;
    display: flex; flex-direction: column; align-items: center; justify-content: center;
    gap: 110px;
  }
  .card {
    position: relative;
    width: 800px; height: 457px;
    overflow: hidden;
  }
  .card-front { background: var(--paper); }
  .card-shapes { position: absolute; inset: 0; }
  .brand {
    position: absolute; left: 58px; top: 83px;
    display: flex; align-items: center; gap: 20px;
  }
  .brand-dot {
    width: 70px; height: 70px; border-radius: 50%;
    background: var(--navy);
  }
  .brand-name {
    font-size: 32px; font-weight: 500; color: var(--navy);
    letter-spacing: 0.5px;
  }
  .contact {
    position: absolute; right: 38px; top: 255px;
    text-align: right; color: var(--ink-light);
  }
  .contact-name { font-size: 29px; font-weight: 500; line-height: 1.1; }
  .contact-role { font-size: 17px; font-weight: 400; margin-bottom: 16px; }
  .contact-line {
    display: flex; justify-content: flex-end; align-items: center; gap: 8px;
    font-size: 18px; line-height: 23px;
  }
  .contact-line svg { width: 15px; height: 15px; fill: var(--ink-light); }
  .contact-address { font-size: 18px; margin-top: 8px; }

  .card-back {
    background: linear-gradient(180deg, var(--navy-light) 0%, var(--navy-deep) 100%);
  }
  .back-texture {
    position: absolute; inset: 0;
    background: radial-gradient(ellipse at 40% 30%, rgba(255,255,255,0.05), rgba(255,255,255,0) 70%);
  }
  .back-brand {
    position: absolute; right: 78px; bottom: 78px;
    display: flex; align-items: center; gap: 16px;
  }
  .back-brand .brand-dot { width: 56px; height: 56px; background: var(--ink-light); }
  .back-brand .brand-name { color: var(--ink-light); font-size: 28px; }
</style>
</head>
<body>
<main class="stage">
  <section class="card card-front">
    <svg class="card-shapes" viewBox="0 0 800 457" width="800" height="457" aria-hidden="true">
      <path fill="var(--swoosh)" d="M228,440 C400,250 600,140 800,158 L800,194 C580,180 400,300 240,457 Z"/>
      <path fill="var(--navy)" d="M240,457 C400,300 580,180 800,194 L800,457 Z"/>
    </svg>
    <div class="brand">
      <span class="brand-dot"></span>
      <span class="brand-name">Ward Compass</span>
    </div>
    <div class="contact">
      <div class="contact-name">Salma Derkaoui</div>
      <div class="contact-role">CEO</div>
      <div class="contact-line">+90 612 348 2071
        <svg viewBox="0 0 24 24"><path d="M6.6 10.8a15 15 0 0 0 6.6 6.6l2.2-2.2a1 1 0 0 1 1-.25 11.4 11.4 0 0 0 3.6.6 1 1 0 0 1 1 1V20a1 1 0 0 1-1 1A17 17 0 0 1 3 4a1 1 0 0 1 1-1h3.5a1 1 0 0 1 1 1c0 1.25.2 2.45.6 3.6a1 1 0 0 1-.25 1z"/></svg>
      </div>
      <div class="contact-line">info@wardcompass-example.com
        <svg viewBox="0 0 24 24"><path d="M2 5h20v14H2z M2 5l10 8 10-8" fill="none" stroke="#fff" stroke-width="0"/><path d="M2 5h20v2l-10 7L2 7z"/><path d="M2 9l10 7 10-7v10H2z"/></svg>
      </div>
      <div class="contact-line">www.wardcompass-example.com
        <svg viewBox="0 0 24 24"><circle cx="12" cy="12" r="10"/><path d="M8 6c2 1 1 3 3 4s0 3 2 4-1 4 1 5" fill="none" stroke="var(--navy)" stroke-width="2"/></svg>
      </div>
      <div class="contact-address">14 Annakhil 3 H.R.B. Rabat, Morocco</div>
    </div>
  </section>

  <section class="card card-back">
    <div class="back-texture"></div>
    <div class="back-brand">
      <span class="brand-dot"></span>
      <span class="brand-name">Ward Compass</span>
    </div>
  </section>
</main>
</body>
</html>
```